Aisle signage for supermarket

Design Isle signs for Indian supermarket. Modern, Clear, legible. Would be nice to use our logo colours. Signs Will be double sided and measure 900mm width x 400mm height. Indian theme would be nice. Attached files shows description to go on each sign.
Font styles to use
Sans Serif
Colors
Designer to choose colors to be used in the design.

```html
<!DOCTYPE html>
<html lang="en">
<head>
<meta charset="utf-8">
<title>Aisle Signage – Supermarket</title>
<link rel="stylesheet" href="https://fonts.googleapis.com/css2?family=Fira+Sans:wght@700;800&display=swap">
<style>
  :root {
    --page: #ffffff;
    --forest: #0b6b3a;
    --forest-deep: #085a30;
    --lime: #8dc63f;
    --lime-soft: #a6d35a;
    --lime-pale: #c3e07c;
    --ink-light: #ffffff;
    --sign-ratio: 900 / 400;
  }
  * { box-sizing: border-box; margin: 0; padding: 0; }
  html, body {
    width: 1200px;
    height: 2620px;
    overflow: hidden;
    background: var(--page);
  }
  .sheet {
    width: 1200px;
    height: 2620px;
    padding: 0 50px;
    display: flex;
    flex-direction: column;
    justify-content: space-evenly;
  }
  .sign-grid {
    display: grid;
    grid-template-columns: 1fr 1fr;
    column-gap: 30px;
    row-gap: 44px;
  }
  .sign {
    position: relative;
    width: 100%;
    aspect-ratio: var(--sign-ratio);
    container-type: size;
    overflow: hidden;
    font-family: "Fira Sans", "Helvetica Neue", Arial, sans-serif;
  }
  .sign__backdrop {
    position: absolute;
    inset: 0;
    width: 100%;
    height: 100%;
    display: block;
  }
  .sign__list {
    position: absolute;
    left: 9.5%;
    top: 28%;
    height: 52%;
    display: flex;
    flex-direction: column;
    justify-content: center;
    list-style: none;
    color: var(--ink-light);
    font-weight: 800;
    font-size: 10.2cqh;
    line-height: 1.5;
    letter-spacing: 0.01em;
    text-transform: uppercase;
    text-shadow: 0.25cqh 0.35cqh 0.6cqh rgba(0, 0, 0, 0.45);
  }
  .sign__list li {
    display: flex;
    align-items: center;
    gap: 0.55em;
  }
  .sign__list li::before {
    content: "";
    width: 0;
    height: 0;
    border-top: 0.3em solid transparent;
    border-bottom: 0.3em solid transparent;
    border-left: 0.42em solid var(--ink-light);
  }
  .aisle-badge {
    position: absolute;
    left: 87%;
    top: 68%;
    width: 23cqh;
    height: 23cqh;
    transform: translate(-50%, -50%);
    display: grid;
    place-items: center;
  }
  .aisle-badge__diamond {
    position: absolute;
    inset: 0;
    width: 100%;
    height: 100%;
  }
  .aisle-badge__number {
    position: relative;
    color: var(--ink-light);
    font-weight: 800;
    font-size: 19cqh;
    line-height: 1;
    text-shadow: 0.2cqh 0.3cqh 0.5cqh rgba(0, 0, 0, 0.3);
  }
  .svg-library { position: absolute; width: 0; height: 0; overflow: hidden; }
</style>
</head>
<body>

<svg class="svg-library" aria-hidden="true" focusable="false">
  <defs>
    <linearGradient id="band-tone" x1="0" y1="0" x2="1" y2="0">
      <stop offset="0" stop-color="#9fd04f"/>
      <stop offset="0.5" stop-color="#b5dc66"/>
      <stop offset="1" stop-color="#9fd04f"/>
    </linearGradient>
    <linearGradient id="panel-tone" x1="0" y1="0" x2="1" y2="1">
      <stop offset="0" stop-color="#0b6b3a"/>
      <stop offset="1" stop-color="#0a6436"/>
    </linearGradient>
    <symbol id="sign-backdrop" viewBox="0 0 900 400" preserveAspectRatio="none">
      <rect width="900" height="400" fill="#8dc63f"/>
      <rect width="900" height="62" fill="url(#band-tone)" role="img" aria-label="Indian mandala pattern band in light greens"/>
      <path d="M0,80 H590 C680,80 760,88 783,116 C800,80 845,52 900,34 V400 H0 Z" fill="url(#panel-tone)"/>
      <path d="M560,400 C600,300 700,250 760,230 C820,210 870,170 900,120 V400 Z" fill="#0d7340" opacity="0.35" role="img" aria-label="Faint paisley ornament in the panel"/>
    </symbol>
    <symbol id="aisle-diamond" viewBox="0 0 100 100">
      <rect x="17" y="17" width="66" height="66" transform="rotate(45 50 50)" fill="#8dc63f"/>
      <rect x="24" y="24" width="52" height="52" transform="rotate(45 50 50)" fill="none" stroke="#0b6b3a" stroke-width="2.5"/>
    </symbol>
  </defs>
</svg>

<main class="sheet">

  <section class="sign sign--feature" aria-label="Aisle 1 sign">
    <svg class="sign__backdrop"><use href="#sign-backdrop"/></svg>
    <ul class="sign__list">
      <li>Biscuits / Cakes</li>
      <li>Tea / Coffe</li>
      <li>Savouries</li>
    </ul>
    <div class="aisle-badge"><svg class="aisle-badge__diamond"><use href="#aisle-diamond"/></svg><span class="aisle-badge__number">1</span></div>
  </section>

  <div class="sign-grid">
    <section class="sign" aria-label="Aisle 1 sign">
      <svg class="sign__backdrop"><use href="#sign-backdrop"/></svg>
      <ul class="sign__list"><li>Juices</li><li>Soft Drinks</li></ul>
      <div class="aisle-badge"><svg class="aisle-badge__diamond"><use href="#aisle-diamond"/></svg><span class="aisle-badge__number">1</span></div>
    </section>
    <section class="sign" aria-label="Aisle 3 sign">
      <svg class="sign__backdrop"><use href="#sign-backdrop"/></svg>
      <ul class="sign__list"><li>Pasta/Vermicelli</li><li>Olives</li><li>Honey</li></ul>
      <div class="aisle-badge"><svg class="aisle-badge__diamond"><use href="#aisle-diamond"/></svg><span class="aisle-badge__number">3</span></div>
    </section>

    <section class="sign" aria-label="Aisle 1 sign">
      <svg class="sign__backdrop"><use href="#sign-backdrop"/></svg>
      <ul class="sign__list"><li>Frozen</li><li>Table/Coooking Sauces</li><li>Dessert Mixes</li></ul>
      <div class="aisle-badge"><svg class="aisle-badge__diamond"><use href="#aisle-diamond"/></svg><span class="aisle-badge__number">1</span></div>
    </section>
    <section class="sign" aria-label="Aisle 3 sign">
      <svg class="sign__backdrop"><use href="#sign-backdrop"/></svg>
      <ul class="sign__list"><li>Oils / Ghee</li><li>Canned Products</li></ul>
      <div class="aisle-badge"><svg class="aisle-badge__diamond"><use href="#aisle-diamond"/></svg><span class="aisle-badge__number">3</span></div>
    </section>

    <section class="sign" aria-label="Aisle 2 sign">
      <svg class="sign__backdrop"><use href="#sign-backdrop"/></svg>
      <ul class="sign__list"><li>Dry Fruits / Nuts</li><li>Lentils / Dall</li></ul>
      <div class="aisle-badge"><svg class="aisle-badge__diamond"><use href="#aisle-diamond"/></svg><span class="aisle-badge__number">2</span></div>
    </section>
    <section class="sign" aria-label="Aisle 3 sign">
      <svg class="sign__backdrop"><use href="#sign-backdrop"/></svg>
      <ul class="sign__list"><li>Household / Laundry</li><li>Clean</li><li>Disposables</li></ul>
      <div class="aisle-badge"><svg class="aisle-badge__diamond"><use href="#aisle-diamond"/></svg><span class="aisle-badge__number">3</span></div>
    </section>

    <section class="sign" aria-label="Aisle 2 sign">
      <svg class="sign__backdrop"><use href="#sign-backdrop"/></svg>
      <ul class="sign__list"><li>Whole Spices</li><li>Ground Spices</li></ul>
      <div class="aisle-badge"><svg class="aisle-badge__diamond"><use href="#aisle-diamond"/></svg><span class="aisle-badge__number">2</span></div>
    </section>
    <section class="sign" aria-label="Aisle 4 sign">
      <svg class="sign__backdrop"><use href="#sign-backdrop"/></svg>
      <ul class="sign__list"><li>Chilled Foods</li><li>Gur/Shakkar</li></ul>
      <div class="aisle-badge"><svg class="aisle-badge__diamond"><use href="#aisle-diamond"/></svg><span class="aisle-badge__number">4</span></div>
    </section>

    <section class="sign" aria-label="Aisle 2 sign">
      <svg class="sign__backdrop"><use href="#sign-backdrop"/></svg>
      <ul class="sign__list"><li>Flours</li><li>Rice</li></ul>
      <div class="aisle-badge"><svg class="aisle-badge__diamond"><use href="#aisle-diamond"/></svg><span class="aisle-badge__number">2</span></div>
    </section>
    <section class="sign" aria-label="Aisle 4 sign">
      <svg class="sign__backdrop"><use href="#sign-backdrop"/></svg>
      <ul class="sign__list"><li>Naan/Bread</li><li>Toiletries</li></ul>
      <div class="aisle-badge"><svg class="aisle-badge__diamond"><use href="#aisle-diamond"/></svg><span class="aisle-badge__number">4</span></div>
    </section>
  </div>

</main>
</body>
</html>
```